Single Page Digital Brochure

We are a Sydney based finance company. We lend money to developers. Please see attached example of what we are looking to have produced. We just need a design which can be posted on LINKEDIN

Target Market(s)

Property Developers who are borrowing money

Industry/Entity Type

Finance

Requirements
Must have
• Australian relevant imagery.

TEXT TO INCLUDE:

New Offering from Ferngate Lending
Nice to have
• Design and colour scheme based around our logo (attached)

Please include the same text as the attachment

Please make the design based loosely on the attachment. But do not copy the attachement
Should not have
• Remove Text: 'Settle in under four days'

```html
<!DOCTYPE html>
<html lang="en">
<head>
<meta charset="utf-8">
<title>Ferngate Lending – New Offering Banner</title>
<link rel="stylesheet" href="https://fonts.googleapis.com/css2?family=Cinzel:wght@600;700&family=Crimson+Text:wght@400;600;700&display=swap">
<style>
  :root {
    --stage: #dcdcdc;
    --brand-green: #1f4a33;
    --ink: #2b2b2b;
    --white: #ffffff;
    --sky-top: #3b4650;
    --sky-warm: #8a7a62;
    --sky-glow: rgba(214,176,130,0.55);
    --city: #5b5a4f;
    --water: #1f4f57;
    --water-deep: #173c44;
  }
  * { box-sizing: border-box; margin: 0; padding: 0; }
  html, body { width: 1200px; height: 792px; overflow: hidden; }
  body { background: var(--stage); position: relative; }

  .banner {
    position: absolute; left: 20px; top: 71px;
    width: 1160px; height: 649px;
    background: var(--white);
    box-shadow: 8px 10px 14px rgba(0,0,0,0.28);
    overflow: hidden;
  }
  .hero-photo {
    position: absolute; left: 0; top: 0; width: 1160px; height: 535px;
    background:
      radial-gradient(ellipse 340px 260px at 1020px 220px, var(--sky-glow) 0%, rgba(214,176,130,0) 100%),
      linear-gradient(180deg, rgba(30,38,44,0.35) 0%, rgba(30,38,44,0.1) 40%, rgba(20,40,44,0.35) 100%),
      linear-gradient(180deg, var(--sky-top) 0%, var(--sky-warm) 30%, var(--city) 48%, var(--water) 66%, var(--water-deep) 100%);
  }
  .headline {
    position: absolute; left: 50px; top: 38px;
    font-family: "Cinzel", serif; font-weight: 700;
    font-size: 58px; line-height: 63px; color: var(--white);
    letter-spacing: 0.5px;
  }
  .headline .cap { font-size: 68px; }
  .tagline {
    position: absolute; left: 48px; top: 339px;
    width: 359px; height: 41px;
    border: 1.5px solid var(--white);
    font-family: "Crimson Text", serif; font-weight: 700;
    font-size: 37px; line-height: 38px; color: var(--white);
    padding-left: 8px; white-space: nowrap;
  }
  .loan-terms {
    position: absolute; top: 388px;
    font-family: "Crimson Text", serif; font-size: 25px; line-height: 31.5px;
    color: var(--white); list-style: none; white-space: nowrap;
  }
  .loan-terms strong { font-weight: 700; }
  .loan-terms--left { left: 51px; }
  .loan-terms--right { left: 343px; }

  .contact {
    position: absolute; left: 50px; top: 557px;
    font-family: "Crimson Text", serif; font-size: 28px; line-height: 31px;
    color: var(--ink); white-space: nowrap;
  }
  .contact strong { color: var(--brand-green); font-weight: 700; }

  .logo-arch { position: absolute; left: 0; top: 0; }
  .brand-name {
    position: absolute; left: 807px; width: 300px; top: 596px;
    text-align: center;
    font-family: "Cinzel", serif; font-weight: 600;
    font-size: 27px; color: var(--brand-green); letter-spacing: 0.5px;
  }
</style>
</head>
<body>
  <section class="banner">
    <div class="hero-photo" role="img" aria-label="Aerial dusk view of Sydney Harbour with the Opera House, city skyline and harbour bridge roadway"></div>

    <h1 class="headline">
      <span class="cap">N</span>EW OFFERING<br>
      <span class="cap">F</span>ROM <span class="cap">F</span>ERNGATE<br>
      <span class="cap">L</span>ENDING.
    </h1>

    <p class="tagline">We did Just last week.</p>

    <ul class="loan-terms loan-terms--left">
      <li><strong>Loan Amount:</strong> $750,000</li>
      <li><strong>Rate:</strong> 7.79%</li>
      <li><strong>Term:</strong> 12 Months</li>
      <li><strong>LVR:</strong> 60%</li>
    </ul>
    <ul class="loan-terms loan-terms--right">
      <li><strong>Repayment:</strong> Capitalised</li>
      <li><strong>Security:</strong> 2x Sydney Residential Properties</li>
      <li><strong>Purpose:</strong> Business Working Capital</li>
    </ul>

    <svg class="logo-arch" width="1160" height="649" viewBox="0 0 1160 649" aria-hidden="true">
      <path d="M812 536 C 850 470, 900 449, 957 449 C 1014 449, 1064 470, 1102 536 Z" fill="#ffffff"/>
      <circle class="brand-dot" cx="957" cy="545" r="30" fill="#1f4a33"/>
    </svg>

    <p class="contact">
      Call today on <strong>0400 123 456</strong> or<br>
      <strong>info@ferngatelending.com.au</strong>
    </p>

    <p class="brand-name">FERNGATE LENDING</p>
  </section>
</body>
</html>
```